Forge Night Club Flyer, need asap for party this weekend

Text is drawn as an attachment

Need a flyer for club night this Saturday. Guaranteed project need quick turnaround. Image attached, and the FORGE logo to be large and detailed like a sign. The dj names KESTREL, MR. HALVORNE, AND DESMOND K. ORLEY can be large too. It's for house/electronic music in a nice classy venue. High Res image attached.

Target Market(s)

21-40 year old house music lovers, club business

Industry/Entity Type

Night Club

Font styles to use
Sans Serif

Colors
ffffff
cadf82
33a6d7
0356a4
fbee3d

Requirements
Must have
• Either the girl in hard hat or tool belt image, or something similar to stick with the Forge theme. Also the dj names needs to be the same size
Nice to have
• Faded image or some lining around the images so it doesn't look like a plain photo. Black and white is good or faded.
Should not have
• Any cursive or anything not professional looking

```html
<!DOCTYPE html>
<html lang="en">
<head>
<meta charset="utf-8">
<title>Forge – House &amp; Tech Workers</title>
<link href="https://fonts.googleapis.com/css2?family=Bebas+Neue&family=Graduate&display=swap" rel="stylesheet">
<style>
  :root {
    --white: #ffffff;
    --lime: #cadf82;
    --sky: #33a6d7;
    --royal: #0356a4;
    --sun: #fbee3d;
    --ink: #0b0b0c;
    --navy: #0c2340;
    --orange: #f47b20;
    --red: #e8423a;
    --stage: #e9e9e9;
  }
  * { margin: 0; padding: 0; box-sizing: border-box; }
  html, body { width: 1200px; height: 1200px; overflow: hidden; background: var(--stage); }
  .flyer {
    position: absolute; left: 50px; top: 240px;
    width: 1100px; height: 720px;
    background: var(--ink); overflow: hidden;
    font-family: "Bebas Neue", "Arial Narrow", sans-serif;
  }
  .flyer-art { position: absolute; inset: 0; width: 1100px; height: 720px; }
  .title-plate {
    position: absolute; left: 575px; top: 38px; width: 430px; height: 130px;
    background: var(--lime);
    display: flex; align-items: center; justify-content: center;
  }
  .title-plate h1 {
    font-family: "Graduate", Georgia, serif; font-weight: 400;
    font-size: 100px; letter-spacing: 4px; color: var(--navy);
    -webkit-text-stroke: 5px var(--navy); paint-order: stroke fill;
    text-shadow: 0 0 0 var(--royal), 2px 2px 0 var(--royal);
    line-height: 1; white-space: nowrap;
  }
  .tagline {
    position: absolute; left: 575px; top: 184px; width: 430px;
    text-align: center; color: var(--sun); font-size: 44px; letter-spacing: 0.5px;
    white-space: nowrap; line-height: 1;
  }
  .tagline .star { color: var(--lime); font-size: 24px; vertical-align: middle; margin: 0 8px; }
  .tagline-rule { position: absolute; left: 590px; top: 238px; width: 400px; height: 2px; background: var(--lime); }
  .lineup {
    position: absolute; left: 618px; top: 262px;
    color: var(--white); font-size: 54px; line-height: 0.92; letter-spacing: 0.5px;
    white-space: nowrap;
  }
  .event-box {
    position: absolute; left: 598px; top: 442px; width: 450px; height: 300px;
    border: 2px solid #3a3a3a;
  }
  .age {
    position: absolute; left: 24px; top: 22px;
    font-family: "Graduate", Georgia, serif; font-size: 76px; line-height: 1;
    color: var(--sun); -webkit-text-stroke: 4px var(--sun); white-space: nowrap;
  }
  .date { position: absolute; left: 198px; top: 18px; color: var(--lime); font-size: 40px; letter-spacing: 1px; white-space: nowrap; line-height: 1; }
  .timing {
    position: absolute; left: 198px; top: 64px; background: var(--royal);
    color: var(--white); font-size: 22px; padding: 3px 10px 1px; letter-spacing: 0.5px;
    white-space: nowrap; line-height: 1.1;
  }
  .rule { position: absolute; left: 30px; width: 390px; height: 2px; background: var(--lime); }
  .rule.top { top: 128px; }
  .rule.bottom { top: 202px; }
  .venue {
    position: absolute; left: 0; top: 138px; width: 450px; text-align: center;
    font-family: "Graduate", Georgia, serif; font-size: 48px; line-height: 1.1; color: var(--white); letter-spacing: 1px;
    -webkit-text-stroke: 2px var(--white); white-space: nowrap;
  }
  .address {
    position: absolute; left: 0; top: 214px; width: 450px; text-align: center;
    color: var(--lime); font-size: 28px; letter-spacing: 0.5px; white-space: nowrap;
  }
</style>
</head>
<body>
  <main class="flyer">
    <svg class="flyer-art" viewBox="0 0 1100 720">
      <defs>
        <linearGradient id="photoTone" x1="0" y1="0" x2="1" y2="1">
          <stop offset="0" stop-color="#f49a2a"/>
          <stop offset="0.35" stop-color="#c98a5e"/>
          <stop offset="0.6" stop-color="#d79a3a"/>
          <stop offset="1" stop-color="#e6b43a"/>
        </linearGradient>
      </defs>
      <polygon fill="#cadf82" points="0,420 300,600 420,690 360,720 0,720"/>
      <polygon fill="#f47b20" points="0,0 330,0 0,210"/>
      <polygon fill="#fbee3d" points="250,0 390,0 60,260 20,240"/>
      <polygon fill="#e8e8ea" points="420,40 560,20 520,110 580,190 510,300 560,380 470,470 430,300"/>
      <polygon fill="#fbee3d" points="420,250 560,360 500,520 430,470"/>
      <polygon fill="url(#photoTone)" role="img"
        aria-label="Photo: woman in shorts wearing a leather tool belt filled with pliers and wrenches"
        points="30,110 250,30 380,0 470,40 470,200 520,310 480,420 420,560 300,700 60,720 20,560 40,380 20,240"/>
      <polygon fill="#f47b20" points="480,640 555,585 540,660"/>
      <polygon fill="#e8423a" points="540,580 580,600 560,660"/>
      <polygon fill="#33a6d7" points="500,690 520,690 508,705"/>
      <polygon fill="#33a6d7" points="540,530 555,532 546,548"/>
      <polygon fill="#e8423a" points="700,720 760,700 770,720"/>
      <polygon fill="#cadf82" points="930,260 960,260 945,272"/>
      <polygon fill="#fbee3d" points="935,300 960,330 925,335"/>
      <polygon fill="#33a6d7" points="895,330 920,322 912,340"/>
      <polygon fill="#33a6d7" points="975,342 985,360 968,356"/>
      <polygon fill="#f47b20" points="1000,275 1100,258 1100,285"/>
      <polygon fill="#33a6d7" points="1080,320 1100,312 1094,334"/>
    </svg>

    <div class="title-plate"><h1>FORGE</h1></div>
    <p class="tagline"><span class="star">★</span>HOUSE &amp; TECH WORKERS<span class="star">★</span></p>
    <div class="tagline-rule"></div>

    <p class="lineup">DJ KESTREL,<br>MR. HALVORNE,<br>AND DESMOND K. ORLEY</p>

    <section class="event-box">
      <span class="age">21+</span>
      <span class="date">SAT 3 . DEC . 2016</span>
      <span class="timing">TIMING : 10:00PM - 02:00AM</span>
      <div class="rule top"></div>
      <p class="venue">KVR LOUNGE</p>
      <div class="rule bottom"></div>
      <p class="address">514 W MERIDIAN AVENUE ASHFORD</p>
    </section>
  </main>
</body>
</html>
```